Business Card Upgrade

I have designed our business card using our new logo. I think it needs imporovements. We used to have two cards for our business. One card was for our software business, and the other was for our consulting business. We are now in the process of combining our websites, marketing, name, and a new logo.

Our goal is to have a really sharp professional logo. One reason I designed the card the way I did was that our Titles are sometimes long, and by separating the person's name and title, it shows up very well and the title can be adjusted no matter how long it is. Sometimes the title can be 4 or 5 words or more.

We really like our logo on black as it shows up very nice. Our PMS colors are as follows: 368C and 459C.

The Designer that will be working with us will need to deliver the following:

The front and back of the Business Card Design will need to be delivered in a high quality JPEG, and
The front and back of the Business Card Design in Illustrator Format .ai
Any fonts will need to be sent to us if they are not standard and are required to open the Illustrator file correctly.

To help us get a good idea of the card with a title, please use the title: " Director of Software Development "

NOTE: The chosen designer will be selected to design our new letterhead within 2 weeks from the closing of this contest.

To help us make sure the card design works with longer titles, please use the followign job title on the card:  

"Director of Software and Product Development"

 

ALL DESIGNERS:

1. I appreciate the different angles you are showing the cards, but please be sure and always show the direct view, so I can see the layout and what the person I hand the card will see.

2. Please do not use white.  Please use off white as I don't care for white cards and they get dirty easy and do not represent the designs well.

Dear Designers,

Please provide samples straight one as a viewer of the card will see.  Some of the angles that are presented make it impossible to tell how everything fits, and sometimes even makes areas look skewed. So, please provide a straight sample view.

Pinnacle 400 company executives such as Vice Presidents, and Directors

Software

• Professional looking Card.

Our customers are Directors, Vice Presidents, and Presidents of companies as large as Pinnacle 400 companies. The card needs to get attention wile still looking professional.

Delivery of the finished product in Illustrator Format with any fonts needed to edit the text or open the file.

The card will be a heavy stock with a soft touch coating for that silk feel.

```html
<!DOCTYPE html>
<html lang="en">
<head>
<meta charset="utf-8">
<title>Crestline Trade Partners – Business Card</title>
<link rel="stylesheet" href="https://fonts.googleapis.com/css2?family=Nunito+Sans:wght@400;600;700&display=swap">
<style>
  :root {
    --stage-light: #ffffff;
    --stage-dark: #a9a9a9;
    --card-black: #050505;
    --brand-green: #6cbf44;
    --brand-gold: #e3d27a;
    --map-green: #3c6a2c;
  }
  * { box-sizing: border-box; margin: 0; padding: 0; }
  html, body { width: 1200px; height: 592px; overflow: hidden; }
  body {
    position: relative;
    font-family: "Nunito Sans", Arial, sans-serif;
    background: radial-gradient(ellipse 70% 75% at 50% 38%, var(--stage-light) 0%, #ededed 45%, var(--stage-dark) 100%);
  }
  .card {
    position: absolute;
    top: 158px;
    width: 516px;
    height: 289px;
    background: var(--card-black);
    box-shadow: 2px 3px 6px rgba(0,0,0,.45);
    overflow: hidden;
  }
  .card--front { left: 68px; }
  .card--back { left: 627px; }

  .brand-name {
    position: absolute;
    left: 0; width: 100%;
    text-align: center;
    color: var(--brand-green);
    font-weight: 700;
    font-size: 32px;
    line-height: 37px;
    letter-spacing: 3px;
    text-transform: uppercase;
  }
  .card--front .brand-name { top: 40px; }
  .card--back .brand-name { top: 96px; }

  .divider-rule {
    position: absolute;
    left: 0; top: 146px;
    width: 100%; height: 4px;
    background: var(--brand-green);
  }

  .person { position: absolute; left: 24px; top: 212px; }
  .person__name {
    color: var(--brand-green);
    font-size: 20px;
    font-weight: 400;
    letter-spacing: .3px;
    text-transform: uppercase;
  }
  .person__title {
    margin-top: 5px;
    color: var(--brand-gold);
    font-size: 12px;
  }

  .contact { position: absolute; left: 280px; top: 177px; color: var(--brand-gold); font-size: 12.5px; }
  .contact__row { display: flex; align-items: center; height: 19.5px; }
  .contact__icon { width: 15px; height: 15px; margin-right: 8px; flex: none; }
  .contact__address { margin-top: 3px; line-height: 20px; }

  .world-map {
    position: absolute;
    left: 30px; top: 6px;
    width: 486px; height: 250px;
    background: radial-gradient(ellipse 55% 55% at 52% 48%, #4f8a38 0%, var(--map-green) 40%, #16280f 80%, transparent 100%);
    opacity: .85;
  }
  .tagline {
    position: absolute;
    left: 0; width: 100%;
    top: 244px;
    text-align: center;
    color: var(--brand-gold);
    font-size: 10.5px;
    line-height: 20px;
    text-transform: uppercase;
    letter-spacing: .2px;
  }
</style>
</head>
<body>
  <section class="card card--front" aria-label="Business card front">
    <div class="brand-name">Crestline<br>Trade Partners</div>

    <div class="divider-rule" aria-hidden="true"></div>

    <div class="person">
      <div class="person__name">Dana Whitfield</div>
      <div class="person__title">Director of Software Development</div>
    </div>

    <div class="contact">
      <div class="contact__row">
        <svg class="contact__icon" viewBox="0 0 16 16" aria-hidden="true">
          <circle cx="8" cy="8" r="8" fill="var(--brand-green)"/>
          <rect x="5.5" y="3.5" width="5" height="9" rx="1" fill="none" stroke="var(--card-black)" stroke-width="1.2"/>
        </svg>
        <span>555.010.2847 (Direct)</span>
      </div>
      <div class="contact__row">
        <svg class="contact__icon" viewBox="0 0 16 16" aria-hidden="true">
          <circle cx="8" cy="8" r="8" fill="var(--brand-green)"/>
          <rect x="4" y="5" width="8" height="6" fill="none" stroke="var(--card-black)" stroke-width="1.1"/>
          <path d="M4 5 L8 8.5 L12 5" fill="none" stroke="var(--card-black)" stroke-width="1.1"/>
        </svg>
        <span>dana@crestlinetrade.com</span>
      </div>
      <div class="contact__row">
        <svg class="contact__icon" viewBox="0 0 16 16" aria-hidden="true">
          <circle cx="8" cy="8" r="8" fill="var(--brand-green)"/>
          <circle cx="8" cy="8" r="4.5" fill="none" stroke="var(--card-black)" stroke-width="1"/>
          <ellipse cx="8" cy="8" rx="2" ry="4.5" fill="none" stroke="var(--card-black)" stroke-width="1"/>
          <path d="M3.5 8 H12.5" stroke="var(--card-black)" stroke-width="1"/>
        </svg>
        <span>www.crestlinetrade.com</span>
      </div>
      <div class="contact__address">418 Harbor View Lane<br>Bayport Al, 36000</div>
    </div>
  </section>

  <section class="card card--back" aria-label="Business card back">
    <div class="world-map" role="img" aria-label="Dark green world map silhouette spanning the card"></div>
    <div class="brand-name">Crestline<br>Trade Partners</div>
    <p class="tagline">The only firm with the experience and expertise to offer<br>every foreign-trade zone solutions</p>
  </section>
</body>
</html>
```